RWT Business Cards

We need to design new business cards for our company. We are a Managed Discretionary Account (MDA) adviser based in Sydney Australia. We have distinct corporate colour pallet which will be provided and various logo formats. I will also include our current business card design as a guide only to what we have accepted previously. The final design should convey financial professionalism and experience as well as the necessary company information.

Target Market(s)

High Net Worth and Professional Investors

Industry/Entity Type

Financial

Font styles to use
Serif

```html
<!DOCTYPE html>
<html lang="en">
<head>
<meta charset="utf-8">
<title>RWT Business Cards</title>
<link href="https://fonts.googleapis.com/css2?family=Tinos:wght@400;700&display=swap" rel="stylesheet">
<style>
  :root {
    --page: #2a2a2a;
    --paper: #ffffff;
    --green: #0c7a3e;
    --green-deep: #0a6a35;
    --ink: #141414;
    --stone: #c8c0a0;
    --sand: #d7c9a4;
  }
  * { box-sizing: border-box; margin: 0; padding: 0; }
  html, body { width: 1200px; height: 1000px; overflow: hidden; }
  body {
    background: var(--page);
    font-family: "Tinos", "Times New Roman", serif;
    display: flex; flex-direction: column; align-items: center; justify-content: center;
    gap: 60px;
  }
  .card { position: relative; width: 720px; height: 411px; overflow: hidden; }

  /* Front */
  .card-front { background: var(--paper); }
  .brand-name {
    position: absolute; top: 40px; left: 200px; width: 440px;
    text-align: center; color: var(--green); font-weight: 700; line-height: 1;
  }
  .brand-name .brand-main { display: block; font-size: 60px; letter-spacing: 1px; }
  .brand-name .brand-sub { display: block; font-size: 26px; letter-spacing: 4px; margin-top: 8px; }
  .name-band {
    position: absolute; top: 180px; left: 30px; width: 446px; height: 48px;
    background: var(--ink); color: #fff; font-size: 24px;
    padding: 10px 0 0 28px;
  }
  .role-tab {
    position: absolute; top: 206px; left: 476px; width: 214px; height: 44px;
    background: var(--green); color: #fff; font-size: 20px;
    text-align: center; padding-top: 11px;
  }
  .contact-box {
    position: absolute; background: var(--stone); color: var(--ink);
    font-size: 18px; line-height: 1.3; text-align: center;
    display: flex; flex-direction: column; align-items: center; justify-content: center; gap: 8px;
  }
  .contact-address { top: 228px; left: 30px; width: 230px; height: 162px; }
  .contact-phone { top: 228px; left: 266px; width: 204px; height: 162px; }
  .contact-online { top: 256px; left: 476px; width: 214px; height: 134px; }
  .contact-box svg { width: 20px; height: 20px; }

  /* Back */
  .card-back { background: var(--paper); padding: 14px; }
  .back-field { position: relative; width: 100%; height: 100%; background: var(--green); }
  .web-address {
    position: absolute; top: 70px; width: 100%; text-align: center;
    color: #fff; font-size: 28px;
  }
  .back-brand {
    position: absolute; top: 125px; width: 100%; text-align: center;
    color: var(--sand); font-weight: 700; line-height: 1;
  }
  .back-brand .brand-main { display: block; font-size: 52px; letter-spacing: 1px; }
  .back-brand .brand-sub { display: block; font-size: 24px; letter-spacing: 4px; margin-top: 8px; }
  .licence-band {
    position: absolute; top: 262px; left: 0; width: 100%; height: 58px;
    background: var(--ink); color: #fff; font-size: 18px;
    text-align: center; padding-top: 19px; letter-spacing: 0.5px;
  }
</style>
</head>
<body>
  <section class="card card-front">
    <div class="brand-name"><span class="brand-main">ROWAN WEST</span><span class="brand-sub">TRUST</span></div>
    <div class="name-band">Liam Porter</div>
    <div class="role-tab">Managing Director</div>
    <div class="contact-box contact-address">
      <svg viewBox="0 0 20 20" aria-hidden="true"><path d="M3 10 L10 3 L17 10 M5 9 V17 H15 V9 M8 17 V12 H12 V17" fill="none" stroke="#333" stroke-width="1.4"/></svg>
      <p>Level 4, 12-14 Harbour Lane<br>Sydney NSW 2000<br>Australia</p>
    </div>
    <div class="contact-box contact-phone">
      <svg viewBox="0 0 20 20" aria-hidden="true"><path d="M3 7 Q10 2 17 7 L15 9 L13 7.5 L7 7.5 L5 9 Z M5 11 H15 L16 17 H4 Z" fill="#333"/><circle cx="10" cy="14" r="1.8" fill="#c8c0a0"/></svg>
      <p>1300 555 018<br>+61 (0)4 5550 1234</p>
    </div>
    <div class="contact-box contact-online">
      <svg viewBox="0 0 20 20" aria-hidden="true"><g fill="none" stroke="#333" stroke-width="1.3"><circle cx="10" cy="10" r="7.5"/><ellipse cx="10" cy="10" rx="3.2" ry="7.5"/><path d="M2.5 10 H17.5 M4 6 H16 M4 14 H16"/></g></svg>
      <p>lp@rowanwest.com.au<br>Chat: liam.porter07</p>
    </div>
  </section>

  <section class="card card-back">
    <div class="back-field">
      <p class="web-address">www.rowanwest.com.au</p>
      <div class="back-brand"><span class="brand-main">ROWAN WEST</span><span class="brand-sub">TRUST</span></div>
      <div class="licence-band">ABN: 12 345 678 &nbsp;|&nbsp; AFSL: 000123</div>
    </div>
  </section>
</body>
</html>
```